Brambury Logistics

Create a modern, simple, Elegant business card design for my business.

Services: Tamo Trucks, Transport, Contract Logistics,

Industry/Entity Type

Business

Contact Information for Business Card

Include all details same as old card plus new website address: www.bramburylogistics.com.au

Requirements
Must have
• Similar colors to Logo.

```html
<!DOCTYPE html>
<html lang="en">
<head>
<meta charset="utf-8">
<title>Brambury Logistics – Business Card</title>
<link href="https://fonts.googleapis.com/css2?family=Montserrat:wght@400;500;600;700&display=swap" rel="stylesheet">
<style>
  :root {
    --page: #e9eaec;
    --charcoal: #3a3b3e;
    --navy: #0e4c86;
    --sky: #1aa6e6;
    --silver: #b9bbbe;
    --ink: #3d4046;
    --white: #ffffff;
  }
  * { box-sizing: border-box; margin: 0; padding: 0; }
  html, body { width: 1200px; height: 900px; overflow: hidden; }
  body {
    background: var(--page);
    font-family: "Montserrat", Arial, sans-serif;
    position: relative;
  }
  .card {
    position: absolute;
    width: 600px;
    height: 340px;
    overflow: hidden;
    box-shadow: 0 10px 30px rgba(0,0,0,.18);
  }
  .card-swoosh { position: absolute; inset: 0; width: 100%; height: 100%; }

  /* Front */
  .card-front { left: 70px; top: 100px; background: var(--charcoal); color: var(--white); }
  .front-brand {
    position: absolute; left: 0; right: 0; top: 78px;
    text-align: center; font-weight: 700; font-size: 40px; letter-spacing: 1px;
  }
  .front-rule {
    position: absolute; left: 150px; width: 300px; top: 142px;
    height: 1px; background: rgba(255,255,255,.45);
  }
  .front-services {
    position: absolute; left: 0; right: 0; top: 160px;
    text-align: center; font-size: 14px; font-weight: 500; letter-spacing: 1px;
  }
  .front-web {
    position: absolute; left: 34px; bottom: 14px;
    font-size: 17px; font-weight: 400; letter-spacing: .3px;
  }
  .front-web strong { font-weight: 700; }

  /* Back */
  .card-back { left: 530px; top: 460px; background: var(--white); color: var(--ink); }
  .back-brand {
    position: absolute; left: 26px; top: 126px; width: 180px;
    display: flex; align-items: center; gap: 8px;
    font-weight: 700; font-size: 17px; color: var(--navy); line-height: 1.15;
  }
  .back-brand .mark { width: 12px; height: 12px; border-radius: 50%; background: var(--sky); flex: none; }
  .back-divider {
    position: absolute; left: 222px; top: 40px; height: 200px;
    width: 1.5px; background: var(--navy);
  }
  .back-details { position: absolute; left: 240px; top: 36px; }
  .person-name { font-size: 22px; font-weight: 700; color: var(--navy); letter-spacing: .5px; }
  .person-role { font-size: 12px; margin-top: 1px; margin-bottom: 8px; }
  .contact-list, .service-list { list-style: none; font-size: 13px; line-height: 1.45; }
  .contact-list li { display: flex; align-items: center; gap: 8px; }
  .contact-list svg { width: 11px; height: 11px; fill: var(--navy); flex: none; }
  .contact-list strong { color: var(--navy); font-weight: 600; }
  .service-list { margin-top: 6px; }
  .service-list li { position: relative; padding-left: 18px; }
  .service-list li::before {
    content: ""; position: absolute; left: 2px; top: 7px;
    width: 6px; height: 6px; border-radius: 50%; background: var(--navy);
  }
</style>
</head>
<body>

<section class="card card-front" aria-label="Business card front">
  <svg class="card-swoosh" viewBox="0 0 600 340" preserveAspectRatio="none" aria-hidden="true">
    <path d="M0,290 C230,275 450,220 600,140 L600,340 L0,340 Z" fill="var(--silver)"/>
    <path d="M0,300 C250,288 470,240 600,170 L600,340 L0,340 Z" fill="var(--navy)"/>
    <path d="M300,262 C420,240 520,205 600,160 L600,172 C520,215 430,248 300,262 Z" fill="var(--sky)"/>
  </svg>
  <div class="front-brand">Brambury Logistics</div>
  <div class="front-rule"></div>
  <p class="front-services">TAMO TRUCKS - TRANSPORT - CONTRACT LOGISTICS</p>
  <p class="front-web">www.<strong>bramburylogistics</strong>.com.au</p>
</section>

<section class="card card-back" aria-label="Business card back">
  <svg class="card-swoosh" viewBox="0 0 600 340" preserveAspectRatio="none" aria-hidden="true">
    <path d="M230,340 C330,320 470,270 600,190 L600,340 Z" fill="var(--silver)"/>
    <path d="M240,340 C360,325 490,285 600,215 L600,340 Z" fill="var(--navy)"/>
    <path d="M330,330 C440,305 530,265 600,225 L600,240 C530,280 450,312 330,330 Z" fill="var(--sky)"/>
  </svg>
  <div class="back-brand"><span class="mark"></span><span>Brambury Logistics</span></div>
  <div class="back-divider"></div>
  <div class="back-details">
    <h1 class="person-name">Marten Holloway</h1>
    <p class="person-role">Director</p>
    <ul class="contact-list">
      <li><svg viewBox="0 0 24 24"><path d="M6.6 10.8a15 15 0 0 0 6.6 6.6l2.2-2.2a1 1 0 0 1 1-.25 11.4 11.4 0 0 0 3.6.57 1 1 0 0 1 1 1V20a1 1 0 0 1-1 1A17 17 0 0 1 3 4a1 1 0 0 1 1-1h3.5a1 1 0 0 1 1 1c0 1.25.2 2.45.57 3.6a1 1 0 0 1-.25 1z"/></svg>0400 555 182</li>
      <li><svg viewBox="0 0 24 24"><path d="M2 5h20v14H2zm2 2v.4l8 5 8-5V7zm0 2.8V17h16V9.8l-8 5z"/></svg>marten@bramburylogistics.com.au</li>
      <li><svg viewBox="0 0 24 24"><path d="M12 2a10 10 0 1 0 0 20 10 10 0 0 0 0-20zm6.9 9h-3a15 15 0 0 0-1.3-5.4A8 8 0 0 1 18.9 11zM12 4c.9 1.2 1.8 3.6 2 7h-4c.2-3.4 1.1-5.8 2-7zM9.4 5.6A15 15 0 0 0 8.1 11h-3a8 8 0 0 1 4.3-5.4zM5.1 13h3a15 15 0 0 0 1.3 5.4A8 8 0 0 1 5.1 13zM12 20c-.9-1.2-1.8-3.6-2-7h4c-.2 3.4-1.1 5.8-2 7zm2.6-1.6a15 15 0 0 0 1.3-5.4h3a8 8 0 0 1-4.3 5.4z"/></svg>www.<strong>bramburylogistics</strong>.com.au</li>
    </ul>
    <ul class="service-list">
      <li>Tamo Trucks</li>
      <li>All General and Oversize Transport</li>
      <li>Specialized Transport</li>
      <li>Contract Logistics</li>
      <li>Express/Hotshot Services</li>
    </ul>
  </div>
</section>

</body>
</html>
```